Crumbly Nibs Label Design [Snack Brand]

We need an updated version of our label. It can either be a new concept or a refreshed take on our existing label. The new label needs to feel more modern. We need an execution in black and white and one in color.

There is a full creative brief attached that we hope will provide plenty of context and inspiration for the project.

Target Market(s)

Millennials and Gen Z: This is likely the most promising demo at the start. It plays well with the brand origin story and students love it. It is where initial word of mouth is likely to originate. Additionally, this demo is considered more adventurous with food choices and enjoy trying new flavors and creative combinations. Foodies and culinary enthusiasts Gift-givers Families

Industry/Entity Type

Food and Snacks

Requirements
Must have
• Any images containing examples of food should contain corn puffs (not popcorn)
Should not have

```html
<!DOCTYPE html>
<html lang="en">
<head>
<meta charset="utf-8">
<title>Crumbly Nibs – Original Caramel Label</title>
<link href="https://fonts.googleapis.com/css2?family=Coustard:wght@400;900&family=Courier+Prime:wght@400;700&family=Archivo:wght@400;700;900&display=swap" rel="stylesheet">
<style>
  :root{
    --ink:#4a2a1f;
    --ink-soft:#7a5a4c;
    --paper:#f3f1ee;
    --panel:#e4dfda;
  }
  *{box-sizing:border-box;margin:0;padding:0}
  html,body{width:1200px;height:1200px;overflow:hidden;background:var(--paper)}
  .label{position:relative;width:1200px;height:1200px;color:var(--ink);font-family:"Courier Prime",monospace}
  .brand{position:absolute;left:110px;top:95px;display:flex;align-items:center;gap:16px}
  .brand-dot{width:26px;height:26px;border-radius:50%;background:var(--ink)}
  .brand-name{font-family:"Coustard",serif;font-weight:900;font-size:72px;line-height:1;white-space:nowrap}
  .formula{position:absolute;left:300px;top:200px;font-family:"Coustard",serif;font-size:40px}
  .formula sub{font-size:20px}
  .flavor{position:absolute;left:110px;top:260px;width:700px;font-family:"Coustard",serif;line-height:.95}
  .flavor .kind{font-size:68px;padding-left:150px}
  .flavor .base{font-size:50px;padding-left:150px}
  .flavor .name{font-size:132px;font-weight:900;margin-top:10px}
  .flavor .taste{font-size:84px;padding-left:110px}
  .story{position:absolute;left:110px;top:610px;width:480px;font-size:15px;line-height:1.35}
  .lettering{position:absolute;left:110px;top:820px;width:220px;height:220px;background:var(--panel);border-radius:6px}
  .netwt{position:absolute;left:110px;top:1058px;font-family:"Archivo",sans-serif;font-weight:900;font-size:22px;line-height:1.15}
  .illustration{position:absolute;left:360px;top:820px;width:450px;height:310px;background:linear-gradient(180deg,#ebe6e1,#d9d1ca);border-radius:6px}
  .facts{position:absolute;left:840px;top:110px;width:260px;border:3px solid var(--ink);padding:8px 10px;font-family:"Archivo",sans-serif;font-size:14px}
  .facts h2{font-weight:900;font-size:30px;line-height:1;border-bottom:1px solid var(--ink);padding-bottom:4px}
  .facts .serv{padding:4px 0;border-bottom:8px solid var(--ink)}
  .facts .serv b{display:flex;justify-content:space-between}
  .facts .cal{display:flex;justify-content:space-between;align-items:flex-end;font-weight:900;font-size:24px;border-bottom:5px solid var(--ink);padding:4px 0}
  .facts .cal small{font-size:12px;display:block}
  .facts .row{display:flex;justify-content:space-between;border-bottom:1px solid var(--ink);padding:3px 0}
  .facts .in{padding-left:14px}
  .facts .dv{text-align:right;font-weight:700;border-bottom:1px solid var(--ink);padding:3px 0}
  .facts .thick{border-bottom:8px solid var(--ink)}
  .facts .note{font-size:11px;line-height:1.3;padding-top:5px}
  .back-panel{position:absolute;left:840px;top:725px;width:270px;display:flex;flex-direction:column;gap:14px}
  .ingredients{font-size:14px;line-height:1.35}
  .contains{font-size:14px;font-weight:700}
  .allergen{font-size:12px;line-height:1.35;font-family:"Archivo",sans-serif}
</style>
</head>
<body>
<main class="label">
  <div class="brand"><span class="brand-dot"></span><span class="brand-name">Crumbly Nibs</span></div>
  <div class="formula">C<sub>6</sub>H<sub>12</sub>O<sub>6</sub></div>

  <div class="flavor">
    <div class="kind">flavored</div>
    <div class="base">cornpuffs</div>
    <div class="name">original</div>
    <div class="taste">caramel</div>
  </div>

  <p class="story">Crumbly Nibs is a delicious snack that became popular after making it for my students the past 10 years as a laboratory demonstration on macromolecules. My goal was to provide my biology students with a fun yet practical example of the chemistry of the foods we consume. After years of requests, the dream of bringing it to market is finally a reality.</p>

  <div class="lettering" role="img" aria-label="Hand-lettered badge reading Made By A Teacher with an apple"></div>
  <div class="netwt">Net Wt<br>7 OZ.<br>(198g)</div>

  <div class="illustration" role="img" aria-label="Line illustration of a teacher in a lab with beakers and flasks of corn puffs"></div>

  <section class="facts">
    <h2>Nutrition Facts</h2>
    <div class="serv">About 6 servings per container<b><span>Serving size</span><span>3/4 cup (33g)</span></b></div>
    <div class="cal"><span><small>Amount Per Serving</small>Calories</span><span>160</span></div>
    <div class="dv">% Daily Value*</div>
    <div class="row"><b>Total Fat 11g</b><span>14%</span></div>
    <div class="row in"><span>Saturated Fat 4.5g</span><span>23%</span></div>
    <div class="row in"><span>Trans Fat 0g</span><span></span></div>
    <div class="row"><b>Cholesterol 20mg</b><span>7%</span></div>
    <div class="row"><b>Sodium 150mg</b><span>7%</span></div>
    <div class="row"><b>Total Carbohydrate 16g</b><span>6%</span></div>
    <div class="row in"><span>Dietary Fiber 0g</span><span>0%</span></div>
    <div class="row in"><span>Total Sugars 13g</span><span></span></div>
    <div class="row in"><span>Includes 13g Added Sugars</span><span>26%</span></div>
    <div class="row thick"><b>Protein 0g</b><span></span></div>
    <div class="row"><span>Vitamin D 0mcg</span><span>0%</span></div>
    <div class="row"><span>Calcium 10mg</span><span>0%</span></div>
    <div class="row"><span>Iron 0.1mg</span><span>0%</span></div>
    <div class="row"><span>Potassium 20mg</span><span>0%</span></div>
    <p class="note">*The % Daily Value (DV) tells you how much a nutrient in a serving of food contributes to a daily diet. 2,000 calories a day is used for general nutrition advice.</p>
  </section>

  <section class="back-panel">
    <p class="ingredients">INGREDIENTS: Corn Puffs (Corn Meal, Vegetable Oil (Corn Oil, Sunflower Oil, Canola Oil and/or Cottonseed Oil), Salt), Butter (Pasteurized Cream, Lactic Acid), Brown Sugar, Corn Syrup, Salt, Vanilla Extract (Vanilla Beans, Water, Alcohol), Baking Soda (Sodium Bicarbonate).</p>
    <p class="contains">CONTAINS: MILK</p>
    <p class="allergen">PRODUCED IN A FACILITY THAT ALSO PROCESSES PEANUTS. THIS PACKAGE IS SOLD BY WEIGHT, NOT VOLUME. CONTENTS MAY SETTLE DURING SHIPPING AND HANDLING.<br>Crumbly Nibs, Larkfield, VA<br>www.crumblynibs-shop.com</p>
  </section>
</main>
</body>
</html>
```